Screendesign für neue Website
Zielgruppe
Bauherren und alle die mal zum Architekten müssen.
Aufgabenstellung
Bei diesem Auftrag handelt es sich um die Erstellung eines Screendesigns für eine Website eines Archtiktenbüros.
Es wird daher ein Layout im PSD-Format erwartet, eine Umsetzung dessen in HTML wird nicht gefordert.

```html
<!DOCTYPE html>
<html lang="de">
<head>
<meta charset="utf-8">
<title>Planungsbüro Gernot Falke</title>
<link rel="stylesheet" href="https://fonts.googleapis.com/css2?family=Mulish:wght@300;400;700&display=swap">
<style>
:root{
  --page-bg:#242120;
  --brand-grey:#9b9b9b;
  --brand-square:#3b3938;
  --frame:#7a7a7a;
  --panel-top:#ffffff;
  --panel-bottom:#d9d9d9;
  --nav-top:#4a4a4a;
  --nav-bottom:#2c2c2c;
  --nav-line:#5c5c5c;
  --nav-text:#e6e6e6;
  --ink:#1a1a1a;
  --mark-white:#ffffff;
}
*{margin:0;padding:0;box-sizing:border-box}
html,body{width:1200px;height:872px;overflow:hidden}
body{background:var(--page-bg);font-family:"Mulish",sans-serif;position:relative}

.brand-square{position:absolute;left:962px;top:60px;width:78px;height:78px;background:var(--brand-square)}
.brand-name{position:absolute;right:162px;top:140px;font-size:30px;font-weight:300;color:var(--brand-grey);letter-spacing:.2px;white-space:nowrap}

.stage{position:absolute;left:129px;top:210px;width:906px;height:429px;border:2px solid var(--frame);overflow:hidden;background:#fff}

.photo-strip{position:absolute;left:0;top:0;height:134px;width:100%;display:flex}
.photo{height:100%}
.photo--1{width:168px;background:linear-gradient(180deg,#a9b8c4 0%,#d8d8d2 45%,#8c6a5e 70%,#6f6f66 100%)}
.photo--2{width:191px;background:linear-gradient(180deg,#b8bcc2 0%,#e4e2dc 50%,#7b6d5f 80%,#4f4f4d 100%)}
.photo--3{width:189px;background:linear-gradient(180deg,#8fa7c4 0%,#e8e6e0 45%,#a8503f 75%,#5d6f76 100%)}
.photo--4{width:171px;background:linear-gradient(180deg,#2f4053 0%,#d8b478 45%,#7d6c55 75%,#4a4a48 100%)}
.photo--5{flex:1;background:linear-gradient(180deg,#7aa0c8 0%,#e6e4df 50%,#8a8a84 80%,#5d6a4e 100%)}

.intro{position:absolute;left:0;top:134px;width:548px;height:295px;background:linear-gradient(180deg,var(--panel-top) 0%,var(--panel-top) 40%,var(--panel-bottom) 100%)}
.side-blank{position:absolute;left:719px;top:134px;right:0;height:295px;background:linear-gradient(180deg,var(--panel-top) 0%,#eeeeee 100%)}

.tagline{list-style:none;color:var(--ink);font-size:22px;font-weight:300;line-height:27px}
.tagline li{position:absolute;white-space:nowrap}
.tagline strong{font-weight:700}
.tagline .l1{left:30px;top:97px}
.tagline .l2{left:198px;top:124px}
.tagline .l3{left:298px;top:151px}
.tagline .l4{left:401px;top:178px}

.main-nav{position:absolute;left:548px;top:134px;width:171px;height:295px;list-style:none}
.main-nav li{height:49.2px;display:flex;align-items:center;justify-content:center;background:linear-gradient(180deg,var(--nav-top),var(--nav-bottom));border-bottom:1px solid var(--nav-line);color:var(--nav-text);font-size:13.5px;letter-spacing:.2px}

.footer-brand{position:absolute;left:129px;top:651px;display:flex;align-items:center;gap:16px}
.footer-brand .square{width:78px;height:78px;background:var(--mark-white)}
.footer-brand span{font-size:18px;font-weight:300;color:var(--brand-grey)}
</style>
</head>
<body>
  <div class="brand-square"></div>
  <div class="brand-name">Planungsbüro Gernot Falke</div>

  <main class="stage">
    <div class="photo-strip">
      <div class="photo photo--1" role="img" aria-label="Foto: weißes Einfamilienhaus mit roter Fassadenfläche"></div>
      <div class="photo photo--2" role="img" aria-label="Foto: modernes Haus mit Glasfront in der Abenddämmerung"></div>
      <div class="photo photo--3" role="img" aria-label="Foto: Wohnhaus mit Terrasse und Pool"></div>
      <div class="photo photo--4" role="img" aria-label="Foto: beleuchteter Pavillon mit Glaswänden"></div>
      <div class="photo photo--5" role="img" aria-label="Foto: weißes Haus mit Satteldach und Garage"></div>
    </div>

    <section class="intro">
      <ul class="tagline">
        <li class="l1"><strong>Architekten</strong> schaffen</li>
        <li class="l2">Lebens - Raum</li>
        <li class="l3">Lebens - Traum</li>
        <li class="l4"><strong>Traum Haus</strong></li>
      </ul>
    </section>

    <ul class="main-nav">
      <li>Unternehmen</li>
      <li>Projekte</li>
      <li>Information</li>
      <li>Aktuelles</li>
      <li>Leistungen</li>
      <li>Kontakt</li>
    </ul>

    <div class="side-blank"></div>
  </main>

  <div class="footer-brand">
    <div class="square"></div>
    <span>Planungsbüro Gernot Falke</span>
  </div>
</body>
</html>
```